Strong, modern, clean Business Card design

Looking for a stunning, but CLEAN business card design. While we are a faith-based organization, we do NOT want this to look religious.

Industry/Entity Type

Non-Profit

Contact Information for Business Card

Dale Munroe | Lead Pastor
dale@BrightHarvestHope.org
970-555-0148
PO Box 7316
Alder Ridge, WY 80571

Font styles to use
Serif
Sans Serif

Requirements
Should not have
• Religious imagery or symbolism

```html
<!DOCTYPE html>
<html lang="en">
<head>
<meta charset="utf-8">
<title>Bright Harvest Church – Business Card</title>
<link rel="stylesheet" href="https://fonts.googleapis.com/css2?family=Cormorant+Garamond:wght@600&family=Montserrat:wght@500;600&family=Open+Sans:wght@400&display=swap">
<style>
  :root {
    --page: #c9ccd0;
    --card: #3a3a3c;
    --card-fold: #2a2a2c;
    --accent: #4b7d98;
    --ink-light: #ffffff;
  }
  * { box-sizing: border-box; margin: 0; padding: 0; }
  html, body {
    width: 1200px; height: 800px; overflow: hidden;
    background: var(--page);
  }
  .card {
    position: absolute; left: 75px; top: 100px;
    width: 1050px; height: 600px;
    background: var(--card);
    overflow: hidden;
    box-shadow: 0 12px 30px rgba(0,0,0,.25);
  }
  .card-shapes { position: absolute; inset: 0; }
  .brand {
    position: absolute; left: 660px; top: 70px; width: 340px;
    display: flex; flex-direction: column; align-items: center;
    color: var(--accent);
    font-family: "Cormorant Garamond", serif; font-weight: 600;
    white-space: nowrap;
  }
  .brand-square {
    width: 72px; height: 72px; border-radius: 9px;
    background: var(--accent); margin-bottom: 14px;
  }
  .brand-name { line-height: 1; text-align: center; }
  .brand-name .line-main { display: block; font-size: 40px; letter-spacing: 1px; }
  .brand-name .line-sub { display: block; font-size: 24px; letter-spacing: 16px; margin-top: 6px; padding-left: 16px; }
  .contact {
    position: absolute; left: 700px; top: 290px;
    list-style: none;
    font-family: "Open Sans", sans-serif; font-size: 21px;
    color: var(--ink-light); line-height: 1.35;
    white-space: nowrap;
  }
  .contact li { display: flex; align-items: flex-start; gap: 14px; margin-bottom: 10px; }
  .contact svg { flex: none; width: 22px; height: 22px; margin-top: 4px; fill: var(--accent); }
  .nameplate {
    position: absolute; left: 130px; top: 432px;
    transform: rotate(-18.6deg); transform-origin: left top;
    font-family: "Montserrat", sans-serif; color: var(--ink-light);
    white-space: nowrap;
  }
  .nameplate .person { font-size: 40px; font-weight: 600; letter-spacing: 1px; line-height: 1.1; }
  .nameplate .role { font-size: 21px; font-weight: 500; letter-spacing: 1px; margin-left: 88px; }
</style>
</head>
<body>
  <div class="card">
    <svg class="card-shapes" width="1050" height="600" viewBox="0 0 1050 600">
      <defs>
        <filter id="fold-shadow" x="-5%" y="-20%" width="110%" height="140%">
          <feGaussianBlur stdDeviation="3"/>
        </filter>
      </defs>
      <g class="folds" stroke="var(--card-fold)" stroke-width="4" filter="url(#fold-shadow)">
        <line x1="0" y1="250" x2="1050" y2="520"/>
        <line x1="0" y1="300" x2="1050" y2="585"/>
      </g>
      <polygon class="name-band" points="0,455 640,240 600,344 0,545" fill="var(--accent)"/>
    </svg>

    <div class="brand">
      <span class="brand-square"></span>
      <span class="brand-name">
        <span class="line-main">BRIGHT HARVEST</span>
        <span class="line-sub">CHURCH</span>
      </span>
    </div>

    <ul class="contact">
      <li>
        <svg viewBox="0 0 24 24"><path d="M6.6 10.8a15.1 15.1 0 0 0 6.6 6.6l2.2-2.2a1 1 0 0 1 1-.25 11.4 11.4 0 0 0 3.6.57 1 1 0 0 1 1 1V20a1 1 0 0 1-1 1A17 17 0 0 1 3 4a1 1 0 0 1 1-1h3.5a1 1 0 0 1 1 1c0 1.25.2 2.45.57 3.57a1 1 0 0 1-.25 1z"/></svg>
        <span>307-555-0148</span>
      </li>
      <li>
        <svg viewBox="0 0 24 24"><path d="M2 5h20v14H2zm2 2v.4l8 5.2 8-5.2V7zm0 2.8V17h16V9.8l-8 5.2z"/></svg>
        <span>dale@BrightHarvestHope.org</span>
      </li>
      <li>
        <svg viewBox="0 0 24 24"><path d="M12 2a7 7 0 0 0-7 7c0 5.2 7 13 7 13s7-7.8 7-13a7 7 0 0 0-7-7zm0 9.5A2.5 2.5 0 1 1 12 6.5a2.5 2.5 0 0 1 0 5z"/></svg>
        <span>PO Box 7316, Alder Ridge<br>WY 80571</span>
      </li>
    </ul>

    <div class="nameplate">
      <div class="person">DALE MUNROE</div>
      <div class="role">Lead Pastor</div>
    </div>
  </div>
</body>
</html>
```